New web page, 2 companies on the one page

A new web page for an engineering consultancy and maintenance management company

Carlow & Associates is the parent company covering the design and consultancy
Viltrop Engineering is the Maintenance and Reliability company

Target Market(s)

Food & Beverage, ingredients Manufacturing
engineering managers

Coding

Coded - Design and coding required

Number of Pages Required

1 page

Font styles to use
Other font styles liked:
• Roboto

Colors
1861ab
85acd3
d0dfed
cee9f5

```html
<!DOCTYPE html>
<html lang="en">
<head>
<meta charset="utf-8">
<title>Viltrop Engineering — Manufacturing Engineering Support</title>
<link href="https://fonts.googleapis.com/css2?family=Michroma&family=Roboto:wght@400;500;700&display=swap" rel="stylesheet">
<style>
:root{
  --blue:#1861ab;
  --blue-mid:#85acd3;
  --blue-pale:#d0dfed;
  --sky-pale:#cee9f5;
  --navy:#0f2a63;
  --ink:#222a33;
  --muted:#5b6470;
  --white:#fff;
}
*{box-sizing:border-box;margin:0;padding:0}
html,body{width:1200px;height:4688px;overflow:hidden;background:#fff}
body{font-family:"Roboto",Arial,sans-serif;color:var(--ink)}
.heading{font-family:"Michroma","Roboto",sans-serif;font-weight:400;letter-spacing:1px;text-transform:uppercase}
.btn{display:inline-flex;align-items:stretch;border:2px solid var(--white);height:30px;font-size:12px}
.btn span{padding:0 16px;display:flex;align-items:center}
.btn i{width:30px;background:var(--white);display:flex;align-items:center;justify-content:center;font-style:normal}
.btn-blue{border-color:var(--blue)}
.btn-blue span{background:var(--blue);color:#fff}
.btn-blue i{background:#fff;color:var(--blue)}
.brand{display:flex;align-items:center;gap:10px;font-family:"Roboto",sans-serif;font-weight:700;font-size:20px;color:#fff;letter-spacing:1px}
.brand-mark{width:26px;height:26px;border-radius:50%;background:var(--blue-mid)}

/* Hero */
.hero{position:relative;height:660px;overflow:hidden}
.hero-photo{position:absolute;inset:0;background:linear-gradient(100deg,#2b2a2a 0%,#4d4a45 35%,#3a5f8f 62%,#1c4f93 80%,#253b5c 100%)}
.hero-shade{position:absolute;inset:0;background:linear-gradient(90deg,rgba(0,0,0,.45),rgba(0,0,0,0) 60%)}
.nav{position:absolute;top:0;left:0;right:0;height:70px;display:flex;align-items:center;padding:0 75px;background:rgba(10,20,35,.35);z-index:2}
.nav ul{list-style:none;display:flex;gap:44px;margin-left:auto;margin-right:40px}
.nav a{color:#fff;font-size:13px;text-decoration:none}
.nav .btn{color:#fff}
.nav .btn i{color:var(--blue)}
.hero-copy{position:absolute;left:105px;top:185px;color:#fff;z-index:2}
.hero-copy h1{font-size:40px;line-height:1.1}
.hero-copy h2{font-size:27px;line-height:1.5}
.hero-copy p{font-size:12px;max-width:540px;margin:10px 0 20px;line-height:1.4}
.hero-copy .btn i{color:var(--blue)}
.hero-cut{position:absolute;left:0;bottom:0;width:1200px;height:120px}
.dots{position:absolute;left:50%;bottom:40px;transform:translateX(-50%);display:flex;gap:10px;align-items:center;z-index:2}
.dots b{width:9px;height:9px;border-radius:50%;background:#2a2f36}
.dots b.on{width:15px;height:15px;background:#fff;border:3px solid #2a2f36}

/* About */
.about{height:440px;display:flex;align-items:center;padding:0 90px;gap:80px}
.about-text{width:500px}
.about-text h2{font-size:32px;margin-bottom:18px}
.about-text p{font-size:13.5px;line-height:1.5;margin-bottom:22px}
.about-photo{position:relative;width:430px;height:285px}
.about-photo::before{content:"";position:absolute;left:18px;top:18px;right:-18px;bottom:-18px;background:var(--blue-mid)}
.about-photo div{position:absolute;inset:0;background:linear-gradient(135deg,#1b3c73,#2f6db5 50%,#0f2a55)}

/* Process */
.process{height:500px;background:var(--blue-pale);text-align:center;padding-top:80px}
.section-title{font-size:30px;display:inline-block;padding-bottom:8px;border-bottom:3px solid var(--blue)}
.process-cards{display:flex;justify-content:center;gap:72px;margin-top:45px}
.step{width:232px;height:320px;background:#fff;box-shadow:0 4px 10px rgba(0,0,0,.12)}
.step-top{height:128px;background:var(--blue);color:#fff;display:flex;flex-direction:column;align-items:center;justify-content:center;gap:12px;font-size:12px}
.step-icon{width:62px;height:62px;border-radius:50%;background:#fff;display:flex;align-items:center;justify-content:center}
.step p{font-size:11.5px;line-height:1.4;color:var(--muted);padding:18px 38px 14px}
.step .more{display:inline-block;border:1px solid var(--blue);color:var(--blue);font-size:10px;padding:3px 16px}

/* Services */
.services{height:1340px;text-align:center;padding-top:80px}
.service-list{margin-top:40px}
.service{display:flex;align-items:center;height:170px;margin:0 auto 0;width:870px;gap:26px;text-align:left}
.service.rev{flex-direction:row-reverse}
.frame{width:450px;height:170px;background:var(--blue);clip-path:polygon(0 0,88% 0,100% 50%,88% 100%,0 100%);padding:5px}
.frame div{width:100%;height:100%;clip-path:polygon(0 0,88% 0,100% 50%,88% 100%,0 100%)}
.rev .frame,.rev .frame div{clip-path:polygon(12% 0,100% 0,100% 100%,12% 100%,0 50%)}
.service-text{width:400px}
.service-text h3{color:var(--blue);font-size:21px;font-weight:700;margin-bottom:12px}
.service-text p{font-size:11.5px;line-height:1.45;color:var(--muted)}
.ph-a{background:linear-gradient(120deg,#5a8cc4,#a9c8e6 60%,#3d6fa8)}
.ph-b{background:linear-gradient(120deg,#7a8c9c,#b9c9d6 50%,#55708c)}
.ph-c{background:linear-gradient(120deg,#c7d2dc,#8598ab 55%,#d7dee5)}
.ph-d{background:linear-gradient(120deg,#9aa1a6,#d7d8d6 50%,#7a7f82)}
.ph-e{background:linear-gradient(120deg,#5f6e7e,#a3afba 50%,#3e4b5a)}
.ph-f{background:linear-gradient(120deg,#7c8a5c,#c95c2c 45%,#e6e6e0 80%)}
.ph-g{background:linear-gradient(120deg,#c95a3a,#3f6b3a 45%,#5d7a52 70%,#243624)}

/* Reviews */
.reviews{height:470px;background:var(--sky-pale);text-align:center;padding-top:50px}
.review-cards{display:flex;justify-content:center;gap:40px;margin-top:38px}
.review{width:290px;height:310px;background:#fff;position:relative}
.review-top{height:190px;background:var(--blue);clip-path:polygon(0 0,100% 0,100% 58%,50% 100%,0 58%);color:#fff;font-size:10.5px;line-height:1.4;padding:30px 52px 0}
.quote{position:absolute;color:#fff;font-size:34px;font-family:Georgia,serif;line-height:1}
.q1{left:14px;top:118px}.q2{right:14px;top:14px}
.avatar{position:absolute;left:50%;top:150px;transform:translateX(-50%);width:70px;height:70px;border-radius:50%;background:linear-gradient(160deg,#c9b7a6,#6c5a4e);border:4px solid #fff}
.review h4{position:absolute;top:232px;left:0;right:0;color:var(--blue);font-size:11px;font-weight:700}
.socials{position:absolute;top:256px;left:0;right:0;display:flex;justify-content:center;gap:8px}
.socials b{width:10px;height:10px;border-radius:50%;background:var(--blue)}

/* Features */
.features{height:520px;position:relative;color:#fff}
.features-bg{position:absolute;inset:0;width:1200px;height:520px}
.features-title{position:absolute;left:138px;top:95px;font-size:30px;padding-bottom:10px;border-bottom:2px solid var(--blue-mid)}
.emblem{position:absolute;left:103px;top:190px;width:300px;height:300px;border-radius:50%;border:2px dashed rgba(255,255,255,.5);display:flex;align-items:center;justify-content:center}
.emblem-core{width:240px;height:240px;border-radius:50%;background:#fff;display:flex;align-items:center;justify-content:center;color:var(--blue);font-weight:700;font-size:28px;letter-spacing:2px}
.view-btn{position:absolute;left:213px;top:460px;border:1px solid #fff;font-size:11px;padding:4px 22px}
.feature{position:absolute;width:380px}
.feature h4{font-size:13px;font-weight:700;margin-bottom:6px}
.feature p{font-size:10.5px;line-height:1.4;opacity:.9}
.lines{position:absolute;inset:0}

/* Contact */
.contact{height:480px;display:flex;align-items:center;justify-content:center}
.contact-card{width:890px;height:380px;display:flex;box-shadow:0 4px 14px rgba(0,0,0,.14);background:#fff}
.contact-photo{width:445px;background:linear-gradient(120deg,#e9e6e2,#c9c2b8 45%,#f2efea)}
.contact-form{flex:1;padding:50px 45px}
.contact-form h2{font-size:28px;margin-bottom:22px}
.field{border:1.5px solid var(--blue-mid);height:32px;font-size:11px;color:var(--muted);padding:9px 10px;margin-bottom:22px}
.field.tall{height:110px}

/* Footer */
.footer{height:278px;background:var(--navy);color:#fff;position:relative;padding:60px 110px 0;display:flex;gap:50px}
.footer-brand{width:330px}
.footer-brand .brand{font-size:24px;margin-bottom:16px}
.footer-brand p{font-size:10px;line-height:1.5;opacity:.85}
.footer h5{font-size:12px;font-weight:700;margin-bottom:14px}
.footer ul{list-style:none;font-size:10px;line-height:2}
.footer li::before{content:"";display:inline-block;width:5px;height:5px;border-radius:50%;background:#fff;margin-right:10px;vertical-align:middle}
.col-quick{width:130px}.col-serv{width:280px}
.subscribe{width:110px;height:22px;background:#fff;font-size:9px;color:var(--muted);padding:5px 8px;margin-bottom:10px}
.footer .socials{position:static;justify-content:flex-start}
.footer .socials b{background:#fff}
.copyright{position:absolute;left:0;right:0;bottom:14px;text-align:center;font-size:10px;opacity:.8;border-top:1px solid rgba(255,255,255,.2);padding-top:10px;margin:0 40px}
</style>
</head>
<body>

<section class="hero">
  <div class="hero-photo" role="img" aria-label="Engineer in hard hat and blue workwear using a tablet on a factory floor"></div>
  <div class="hero-shade"></div>
  <nav class="nav">
    <div class="brand"><span class="brand-mark"></span>VILTROP</div>
    <ul><li><a href="#">Home</a></li><li><a href="#">About</a></li><li><a href="#">Process</a></li><li><a href="#">Services</a></li><li><a href="#">Reviews</a></li><li><a href="#">Contact</a></li></ul>
    <a class="btn"><span>Detail More</span><i>»</i></a>
  </nav>
  <div class="hero-copy">
    <h1 class="heading">Manufacturing</h1>
    <h2 class="heading">Engineering Support<br>Organisation</h2>
    <p>Lorem ipsum dolor sit amet, consectetur adipiscing elit. Scelerisque pellentesque sollicitudin diam vitae consectetur elit sit.</p>
    <a class="btn"><span>Learn More</span><i>»</i></a>
  </div>
  <svg class="hero-cut" viewBox="0 0 1200 120" preserveAspectRatio="none"><polygon points="0,0 600,120 1200,0 1200,120 0,120" fill="#fff"/></svg>
  <div class="dots"><b></b><b></b><b class="on"></b><b></b><b></b></div>
</section>

<section class="about">
  <div class="about-text">
    <h2 class="heading">About Us</h2>
    <p>Carlow &amp; Associates is specialised manufacturing engineering support organisation that can provide fast, nimble, and flexible services. We have a proven track record in delivering tangible outcomes in process design and fit-out, project management, manufacturing process and maintenance design and execution. Our specialist focus in food manufacturing across a range of sectors allows our team to deliver real benefits to performance and recognition of the clients investment</p>
    <a class="btn btn-blue"><span>Read More</span><i>»</i></a>
  </div>
  <div class="about-photo"><div role="img" aria-label="Smiling engineer in hard hat giving a thumbs up beside machinery"></div></div>
</section>

<section class="process">
  <h2 class="heading section-title">Process</h2>
  <div class="process-cards">
    <div class="step"><div class="step-top"><span class="step-icon"><svg width="32" height="32" viewBox="0 0 32 32" fill="none" stroke="#1861ab" stroke-width="2"><path d="M4 16l6-6 6 4 6-4 6 6-8 8-4-3-4 3z"/></svg></span>STEP 01</div><p>Lorem ipsum dolor sit amet, consectetur adipiscing elit. Id natoque suspendisse donec quis urna. Rhoncus risus sagittis pellentesque. Mauris velit diam et pulvinar.</p><span class="more">Learn More</span></div>
    <div class="step"><div class="step-top"><span class="step-icon"><svg width="32" height="32" viewBox="0 0 32 32" fill="none" stroke="#1861ab" stroke-width="2"><circle cx="12" cy="12" r="6"/><circle cx="21" cy="21" r="6"/></svg></span>STEP 02</div><p>Lorem ipsum dolor sit amet, consectetur adipiscing elit. Id natoque suspendisse donec quis urna. Rhoncus risus sagittis pellentesque. Mauris velit diam et pulvinar.</p><span class="more">Learn More</span></div>
    <div class="step"><div class="step-top"><span class="step-icon"><svg width="32" height="32" viewBox="0 0 32 32" fill="none" stroke="#1861ab" stroke-width="2"><rect x="8" y="5" width="16" height="22" rx="2"/><path d="M12 16l3 3 6-6"/></svg></span>STEP 03</div><p>Lorem ipsum dolor sit amet, consectetur adipiscing elit. Id natoque suspendisse donec quis urna. Rhoncus risus sagittis pellentesque. Mauris velit diam et pulvinar.</p><span class="more">Learn More</span></div>
  </div>
</section>

<section class="services">
  <h2 class="heading section-title">Our Services</h2>
  <div class="service-list">
    <div class="service"><div class="frame"><div class="ph-a" role="img" aria-label="Food technician in protective clothing checking a tablet"></div></div><div class="service-text"><h3>Major Equipment</h3><p>Lorem ipsum dolor sit amet, consectetur adipiscing elit. Nulla sed cum nunc, egestas placerat vulputate id vitae. A id pellentesque suspendisse tortor mi elementum interdum mauris venenatis lorem ipsum dolor sit amet, adipiscing elit vitae.</p></div></div>
    <div class="service rev"><div class="frame"><div class="ph-b" role="img" aria-label="Worker in hairnet operating stainless steel production machinery"></div></div><div class="service-text"><h3>Maintenance Execution</h3><p>Lorem ipsum dolor sit amet, consectetur adipiscing elit. Nulla sed cum nunc, egestas placerat vulputate id vitae. A id pellentesque suspendisse tortor mi elementum interdum mauris venenatis lorem ipsum dolor sit amet, adipiscing elit vitae.</p></div></div>
    <div class="service"><div class="frame"><div class="ph-c" role="img" aria-label="Technician in protective suit inspecting process tanks"></div></div><div class="service-text"><h3>Maintenance Management</h3><p>Lorem ipsum dolor sit amet, consectetur adipiscing elit. Nulla sed cum nunc, egestas placerat vulputate id vitae. A id pellentesque suspendisse tortor mi elementum interdum mauris venenatis lorem ipsum dolor sit amet, adipiscing elit vitae.</p></div></div>
    <div class="service rev"><div class="frame"><div class="ph-d" role="img" aria-label="Stainless steel vessels being installed in a clean plant room"></div></div><div class="service-text"><h3>Installation &amp; Commissioning</h3><p>Lorem ipsum dolor sit amet, consectetur adipiscing elit. Nulla sed cum nunc, egestas placerat vulputate id vitae. A id pellentesque suspendisse tortor mi elementum interdum mauris venenatis lorem ipsum dolor sit amet, adipiscing elit vitae.</p></div></div>
    <div class="service"><div class="frame"><div class="ph-e" role="img" aria-label="Industrial plant with automated pipework and control systems"></div></div><div class="service-text"><h3>SCADA</h3><p>Lorem ipsum dolor sit amet, consectetur adipiscing elit. Nulla sed cum nunc, egestas placerat vulputate id vitae. A id pellentesque suspendisse tortor mi elementum interdum mauris venenatis lorem ipsum dolor sit amet, adipiscing elit vitae.</p></div></div>
    <div class="service rev"><div class="frame"><div class="ph-f" role="img" aria-label="Camera based vision inspection unit scanning packaged products"></div></div><div class="service-text"><h3>Vision Inspection Systems</h3><p>Lorem ipsum dolor sit amet, consectetur adipiscing elit. Nulla sed cum nunc, egestas placerat vulputate id vitae. A id pellentesque suspendisse tortor mi elementum interdum mauris venenatis lorem ipsum dolor sit amet, adipiscing elit vitae.</p></div></div>
    <div class="service"><div class="frame"><div class="ph-g" role="img" aria-label="Engineer in hard hat working beside green industrial valves"></div></div><div class="service-text"><h3>Manufacturing Performance</h3><p>Lorem ipsum dolor sit amet, consectetur adipiscing elit. Nulla sed cum nunc, egestas placerat vulputate id vitae. A id pellentesque suspendisse tortor mi elementum interdum mauris venenatis lorem ipsum dolor sit amet, adipiscing elit vitae.</p></div></div>
  </div>
</section>

<section class="reviews">
  <h2 class="heading section-title">Reviews</h2>
  <div class="review-cards">
    <div class="review"><div class="review-top">Lorem ipsum dolor sit amet, consectetur adipiscing elit. Nulla sed cum nunc, egestas placerat vulputate id vitae a id pellentesque suspendisse tortor mi elementum interdum</div><span class="quote q1">“</span><span class="quote q2">”</span><div class="avatar" role="img" aria-label="Client portrait"></div><h4>DAN PORTER</h4><div class="socials"><b></b><b></b><b></b></div></div>
    <div class="review"><div class="review-top">Lorem ipsum dolor sit amet, consectetur adipiscing elit. Nulla sed cum nunc, egestas placerat vulputate id vitae a id pellentesque suspendisse tortor mi elementum interdum</div><span class="quote q1">“</span><span class="quote q2">”</span><div class="avatar" role="img" aria-label="Client portrait"></div><h4>DAN PORTER</h4><div class="socials"><b></b><b></b><b></b></div></div>
    <div class="review"><div class="review-top">Lorem ipsum dolor sit amet, consectetur adipiscing elit. Nulla sed cum nunc, egestas placerat vulputate id vitae a id pellentesque suspendisse tortor mi elementum interdum</div><span class="quote q1">“</span><span class="quote q2">”</span><div class="avatar" role="img" aria-label="Client portrait"></div><h4>DAN PORTER</h4><div class="socials"><b></b><b></b><b></b></div></div>
  </div>
</section>

<section class="features">
  <svg class="features-bg" viewBox="0 0 1200 520" preserveAspectRatio="none"><polygon points="0,0 1200,0 1200,440 600,520 0,440" fill="#1861ab"/></svg>
  <svg class="lines" viewBox="0 0 1200 520" fill="none" stroke="rgba(255,255,255,.45)" stroke-dasharray="4 4"><path d="M420 210L590 145"/><path d="M430 290L640 265"/><path d="M430 360L610 390"/><path d="M420 430L500 455"/></svg>
  <h2 class="heading features-title">Features</h2>
  <div class="emblem"><div class="emblem-core">VILTROP</div></div>
  <span class="view-btn">View detail</span>
  <div class="feature" style="left:640px;top:80px"><h4>Performance Measurement</h4><p>Lorem ipsum dolor sit amet, consectetur adipiscing elit. Sed sed in imperdiet integer. Eleifend enim, mauris odio fringilla ultrices scelerisque montes, tempus. Condimentum mi faucibus et vestibulum cursus.</p></div>
  <div class="feature" style="left:700px;top:195px"><h4>Performance Measurement</h4><p>Lorem ipsum dolor sit amet, consectetur adipiscing elit. Sed sed in imperdiet integer. Eleifend enim, mauris odio fringilla ultrices scelerisque montes, tempus. Condimentum mi faucibus et vestibulum cursus.</p></div>
  <div class="feature" style="left:665px;top:320px"><h4>Performance Measurement</h4><p>Lorem ipsum dolor sit amet, consectetur adipiscing elit. Sed sed in imperdiet integer. Eleifend enim, mauris odio fringilla ultrices scelerisque montes, tempus. Condimentum mi faucibus et vestibulum cursus.</p></div>
  <div class="feature" style="left:530px;top:420px"><h4>Performance Measurement</h4><p>Lorem ipsum dolor sit amet, consectetur adipiscing elit. Sed sed in imperdiet integer. Eleifend enim, mauris odio fringilla ultrices scelerisque montes, tempus. Condimentum mi faucibus et vestibulum cursus.</p></div>
</section>

<section class="contact">
  <div class="contact-card">
    <div class="contact-photo" role="img" aria-label="Two customer support agents with headsets at a laptop"></div>
    <form class="contact-form">
      <h2 class="heading">Contact Us</h2>
      <div class="field">Your Name</div>
      <div class="field">Email Address</div>
      <div class="field">Phone number</div>
      <div class="field tall">Message</div>
      <span class="btn btn-blue"><span>Submit</span><i>»</i></span>
    </form>
  </div>
</section>

<footer class="footer">
  <div class="footer-brand">
    <div class="brand"><span class="brand-mark"></span>VILTROP</div>
    <p>Viltrop is a full service engineering partner helping food and beverage plants with maintenance, reliability, operations, and design teams. From planning and execution to long term strategies, we help improve plant performance.</p>
  </div>
  <div class="col-quick"><h5>QUICK LINKS</h5><ul><li>Home</li><li>About us</li><li>Services</li><li>Contact</li></ul></div>
  <div class="col-serv"><h5>SERVICES</h5><ul><li>Process &amp; Facilities Design</li><li>Project Management</li><li>Major Equipment and Services</li><li>Contact</li><li>Engineering &amp; Maintenance Management</li><li>Maintenance Execution</li><li>Manufacturing Performance Measurement</li><li>SCADA</li></ul></div>
  <div><h5>SOCIAL LINKS</h5><div class="subscribe">email</div><div class="socials"><b></b><b></b><b></b><b></b></div></div>
  <p class="copyright">© 2021 Viltrop Engineering Reliability Pty. All rights reserved.</p>
</footer>

</body>
</html>
```